Business Card Design Project

Basic business card with minimal details. I just need company name, email & web address, telephone and my name.
I would like the back of the card to be grey with my logo & company name centred.

Target Market(s)

Architects
Builders
Property Developers

Industry/Entity Type

Business

Font styles to use
Sans Serif

Colors

Designer to choose colors to be used in the design.

Requirements
Must have
• Framewise Build
Marcus Helby - Director
M: 0427 593184
E: marcus@framewisebuild.com.au
W: www.framewisebuild.com.au
Should not have
• No other images or pictures

```html
<!DOCTYPE html>
<html lang="en">
<head>
<meta charset="utf-8">
<title>Framewise Build – Business Card</title>
<link rel="stylesheet" href="https://fonts.googleapis.com/css2?family=Tinos:wght@400;700&display=swap">
<style>
  :root {
    --backdrop: #e7e7e9;
    --card-front: #f7f7f7;
    --card-back: #151515;
    --crimson: #9c1536;
    --ink: #1e1e1e;
    --ink-soft: #3a3a3a;
    --rule: #2a2a2a;
    --white: #f2f2f2;
  }
  * { box-sizing: border-box; margin: 0; padding: 0; }
  html, body {
    width: 1200px;
    height: 1200px;
    overflow: hidden;
    background: var(--backdrop);
    font-family: "Tinos", "Times New Roman", serif;
  }
  .canvas {
    width: 1200px;
    height: 1200px;
    display: flex;
    flex-direction: column;
    align-items: center;
    justify-content: center;
    gap: 72px;
  }
  .card {
    width: 760px;
    height: 434px;
    box-shadow: 0 14px 34px rgba(0,0,0,0.14), 0 2px 6px rgba(0,0,0,0.08);
    position: relative;
  }
  /* Front */
  .card--front {
    background: var(--card-front);
    display: flex;
    align-items: center;
  }
  .front__brand {
    width: 320px;
    display: flex;
    align-items: center;
    justify-content: center;
    gap: 14px;
  }
  .brand-mark {
    width: 26px;
    height: 26px;
    background: var(--crimson);
    flex: none;
  }
  .brand-name {
    font-weight: 700;
    font-size: 28px;
    color: var(--ink);
    letter-spacing: 0.04em;
    text-transform: uppercase;
  }
  .front__divider {
    width: 1.5px;
    height: 150px;
    background: var(--rule);
    flex: none;
  }
  .front__details {
    padding-left: 52px;
    color: var(--ink);
  }
  .person-name {
    font-size: 36px;
    font-weight: 700;
    color: var(--crimson);
    line-height: 1.05;
  }
  .person-role {
    font-size: 24px;
    font-weight: 700;
    color: var(--ink-soft);
    margin-top: 2px;
    margin-bottom: 12px;
  }
  .contact-list { list-style: none; }
  .contact-list li {
    font-size: 18px;
    line-height: 1.5;
    color: var(--ink);
  }
  /* Back */
  .card--back {
    background: var(--card-back);
    display: flex;
    flex-direction: column;
    align-items: center;
    justify-content: center;
    gap: 30px;
  }
  .card--back .brand-mark {
    width: 96px;
    height: 96px;
  }
  .card--back .brand-name {
    color: var(--white);
    font-size: 46px;
    letter-spacing: 0.06em;
  }
</style>
</head>
<body>
  <main class="canvas">
    <section class="card card--front" aria-label="Business card front">
      <div class="front__brand">
        <span class="brand-mark" aria-hidden="true"></span>
        <span class="brand-name">Framewise Build</span>
      </div>
      <div class="front__divider" aria-hidden="true"></div>
      <div class="front__details">
        <h1 class="person-name">Marcus Helby</h1>
        <p class="person-role">Director</p>
        <ul class="contact-list">
          <li>M: 0427 593184</li>
          <li>E: marcus@framewisebuild.com.au</li>
          <li>W: www.framewisebuild.com.au</li>
        </ul>
      </div>
    </section>

    <section class="card card--back" aria-label="Business card back">
      <span class="brand-mark" aria-hidden="true"></span>
      <span class="brand-name">Framewise Build</span>
    </section>
  </main>
</body>
</html>
```